Wavelink Earphone Packaging Design

We want to use the packaging for 4-5 of our Wavelink Earphone series (Picture enclosed) and hence we would not like to put any product pictures on the packaging.

Material: E-Flute Paper box
Type: Window Box style
Design features we prefer: Colorful, creative, trendy, High tech.
Requirement: AI file is preferred
Size of Packaging: (L) 95 x (W) 40 x (H) 120 mm

Enclosed are a detailed description along with competitor designs for your reference.

Any further questions, please feel free to ask

```html
<!DOCTYPE html>
<html lang="en">
<head>
<meta charset="utf-8">
<title>Wavelink Earphone 5.0 – Box Dieline</title>
<link rel="stylesheet" href="https://fonts.googleapis.com/css2?family=Jost:wght@300;400;500&family=Roboto:wght@400;700&family=Oswald:wght@600&display=swap">
<style>
  :root{
    --bg:#ecf0ef;
    --ink:#111111;
    --lime:#8cff00;
    --paper:#ffffff;
  }
  html,body{margin:0;padding:0;width:1200px;height:1200px;overflow:hidden;background:var(--bg);}
  .dieline{position:absolute;left:0;top:107px;width:1200px;height:985px;display:block;}
  .title{font-family:'Jost',sans-serif;}
  .title-light{font-weight:300;}
  .title-mid{font-weight:500;}
  .lime{fill:var(--lime);}
  .ink{fill:var(--ink);}
  .paper{fill:var(--paper);}
  .spec{font-family:'Roboto',sans-serif;font-size:7.6px;fill:#fff;}
  .spec-head{font-family:'Roboto',sans-serif;font-size:9px;font-weight:700;fill:var(--lime);}
  .spec-val{font-weight:700;}
  .small{font-family:'Roboto',sans-serif;font-size:6.4px;fill:#fff;}
  .badge-label{font-family:'Oswald',sans-serif;font-size:5.4px;fill:var(--ink);text-anchor:middle;}
  .powered{font-family:'Roboto',sans-serif;font-size:4.6px;font-weight:700;text-anchor:middle;}
  .brand{font-family:'Roboto',sans-serif;font-size:10.5px;font-weight:700;text-anchor:middle;}
  .company{font-family:'Jost',sans-serif;font-size:11px;font-weight:500;text-anchor:middle;letter-spacing:.6px;}
  .bracket{fill:none;stroke-width:1.2;}
</style>
</head>
<body>
<svg class="dieline" viewBox="335 820 815 670" xmlns="http://www.w3.org/2000/svg" aria-label="Flat dieline of the Wavelink Earphone 5.0 window box">

  <!-- Top tuck lid -->
  <g class="panel-lid">
    <path class="ink" d="M462,834 H716 Q722,834 722,840 V866 L724,868 V1012 H455 V868 L457,866 V840 Q457,834 462,834 Z"/>
    <g class="title" transform="translate(590,930) rotate(180)">
      <text x="-80" y="-2" class="title-light" font-size="20" fill="#fff">Wavelink</text>
      <text x="-80" y="20" class="title-mid" font-size="20" fill="#fff">Earphone</text>
      <text x="14" y="20" class="title-light lime" font-size="40">5.0</text>
    </g>
  </g>

  <!-- Front panel -->
  <g class="panel-front">
    <rect class="paper" x="455" y="1012" width="268" height="230"/>
    <path class="ink" d="M505,1012 H672 L689,1078 Q693,1097 672,1097 H507 Q486,1097 490,1078 Z" stroke="var(--lime)" stroke-width="2.5"/>
    <g stroke="#fff" class="bracket">
      <path d="M538,1042 V1036 H544 M634,1036 H640 V1042 M538,1068 V1074 H544 M634,1074 H640 V1068"/>
    </g>
    <text x="589" y="1056" class="company lime">Company Name</text>

    <g class="title">
      <text x="492" y="1180" class="title-light ink" font-size="23">Wavelink</text>
      <text x="492" y="1206" class="title-mid ink" font-size="23">Earphone</text>
      <text x="608" y="1206" class="title-light lime" font-size="50">5.0</text>
    </g>

    <path class="ink" d="M455,1240 H723 V1438 H712 V1475 H466 V1438 H455 Z"/>
    <path d="M455,1240 H723" stroke="var(--lime)" stroke-width="2"/>

    <g class="badges">
      <g transform="translate(520,1268)">
        <polygon class="lime" points="0,-28 24,-14 24,14 0,28 -24,14 -24,-14"/>
        <circle cx="0" cy="-11" r="3" fill="var(--ink)"/>
        <text class="badge-label" y="3">Wavelink</text>
        <text class="badge-label" y="10">5.0</text>
      </g>
      <g transform="translate(589,1268)">
        <polygon class="lime" points="0,-28 24,-14 24,14 0,28 -24,14 -24,-14"/>
        <path d="M-5,-14 h3 l4,-3 v8 l-4,-3 h-3 z M4,-16 q3,3 0,6" fill="var(--ink)" stroke="var(--ink)" stroke-width=".8"/>
        <text class="badge-label" y="3">Exceptional</text>
        <text class="badge-label" y="10">Sound Quality</text>
      </g>
      <g transform="translate(658,1268)">
        <polygon class="lime" points="0,-28 24,-14 24,14 0,28 -24,14 -24,-14"/>
        <rect x="-2" y="-18" width="4" height="7" rx="2" fill="var(--ink)"/>
        <path d="M-4,-13 q4,5 8,0 M0,-10 v3" fill="none" stroke="var(--ink)" stroke-width=".8"/>
        <text class="badge-label" y="3">High Definition</text>
        <text class="badge-label" y="10">Microphone</text>
      </g>
    </g>

    <text x="589" y="1316" class="powered" fill="#fff">POWERED BY</text>
    <circle cx="564" cy="1329" r="3.5" fill="#fff"/>
    <text x="593" y="1333" class="brand" fill="#fff">Wavelink</text>
  </g>

  <!-- Left side panel -->
  <g class="panel-side-left">
    <polygon class="lime" points="355,955 440,955 455,1012 455,1380 395,1425 368,1425 368,1400 342,1400 342,1000"/>
    <g stroke="var(--ink)" class="bracket">
      <path d="M358,1047 V1041 H364 M432,1041 H438 V1047 M358,1064 V1070 H364 M432,1070 H438 V1064"/>
    </g>
    <text x="398" y="1057" class="company ink" font-size="9">Company Name</text>
    <g class="title" transform="translate(388,1257) rotate(-90)">
      <text x="0" y="0" class="title-light ink" font-size="18">Wavelink</text>
      <text x="0" y="19" class="title-mid ink" font-size="18">Earphone</text>
      <text x="86" y="21" class="title-mid ink" font-size="42">5.0</text>
    </g>
    <text x="398" y="1306" class="powered ink">POWERED BY</text>
    <circle cx="374" cy="1319" r="3.5" fill="var(--ink)"/>
    <text x="402" y="1323" class="brand ink">Wavelink</text>
  </g>

  <!-- Right side panel -->
  <g class="panel-side-right">
    <polygon class="lime" points="728,955 823,955 837,1000 837,1400 812,1400 812,1425 785,1425 725,1380 725,1012"/>
    <g class="title" transform="translate(793,1038) rotate(90)">
      <text x="0" y="0" class="title-light ink" font-size="22">Wavelink</text>
      <text x="0" y="28" class="title-mid ink" font-size="22">Earphone</text>
      <text x="142" y="18" class="title-mid ink" font-size="52">5.0</text>
    </g>
    <text x="782" y="1306" class="powered ink">POWERED BY</text>
    <circle cx="758" cy="1319" r="3.5" fill="var(--ink)"/>
    <text x="786" y="1323" class="brand ink">Wavelink</text>
  </g>

  <!-- Back panel -->
  <g class="panel-back">
    <path class="ink" d="M838,1012 H943 V958 Q943,955 946,955 H997 Q1000,955 1000,958 V1012 H1105 L1140,1033 V1332 L1070,1418 V1475 H902 V1418 L838,1350 Z"/>

    <text x="852" y="1035" class="spec-head">Specification</text>
    <g class="spec">
      <text x="852" y="1053">Wavelink Version</text><text x="975" y="1053" class="spec-val">: 5.0</text>
      <text x="852" y="1067">Wireless Playback Duration</text><text x="975" y="1067" class="spec-val">: 3 - 4 h</text>
      <text x="852" y="1081">Standby Time</text><text x="975" y="1081" class="spec-val">: 80 h</text>
      <text x="852" y="1095">Wireless Range</text><text x="975" y="1095" class="spec-val">: 10 m</text>
      <text x="852" y="1110">Impedance</text><text x="975" y="1110" class="spec-val">: 32 Ω</text>
      <text x="852" y="1124">Sound Pressure Level</text><text x="975" y="1124" class="spec-val">: 100dB ± 3dB</text>
      <text x="852" y="1138">Frequency Response</text><text x="975" y="1138" class="spec-val">: 20 - 20kHz</text>
      <text x="852" y="1152">Driver Unit</text><text x="975" y="1152" class="spec-val">: 10mm</text>
    </g>

    <text x="852" y="1172" class="spec-head" font-size="7.8">Caution</text>
    <g class="small">
      <text x="852" y="1186">Lorem ipsum dolor sit amet, consectetur adipiscing elit. Curabitur</text>
      <text x="852" y="1196">dapibus vitae mauris consectetur fermentum. Pellentesque</text>
      <text x="852" y="1206">eleifend vel orci non tristique.</text>
    </g>

    <g stroke="#fff" class="bracket">
      <path d="M852,1234 V1227 H859 M958,1227 H965 V1234 M852,1275 V1282 H859 M958,1282 H965 V1275"/>
    </g>

    <g class="small" font-size="5.6">
      <text x="979" y="1229" class="lime">© 2019 Lorem ipsum dolor sit amet,</text>
      <text x="979" y="1239">consectetur adipiscing elit. Curabitur</text>
      <text x="979" y="1249">dapibus vitae mauris consectetur</text>
      <text x="979" y="1259">fermentum. Pellentesque eleifend vel</text>
      <text x="979" y="1269">orci non tristique. Donec a orci luctus,</text>
      <text x="979" y="1279">bibendum leo a, hendrerit nunc.</text>
    </g>

    <line x1="852" y1="1298" x2="1093" y2="1298" stroke="#fff" stroke-width="1"/>

    <g class="marks" fill="#fff">
      <rect x="852" y="1316" width="30" height="20" rx="2"/>
      <rect x="892" y="1316" width="30" height="20" rx="2"/>
      <polygon points="950,1314 965,1337 935,1337"/>
      <circle cx="988" cy="1326" r="10"/>
      <rect x="1014" y="1314" width="14" height="22" rx="1"/>
      <polygon points="1051,1315 1061,1334 1041,1334"/>
      <circle cx="1081" cy="1326" r="11"/>
    </g>
  </g>
</svg>
</body>
</html>
```